Dog care service needs business card design

Our company is Paws Harbour. We provide care for dogs while their owners are away, either through home visits or a holiday stay in the homes of carefully selected minders. Our existing website & Chatterbook cover should provide all the colour cues for our business cards - namely blues, blondes and grey. We have an existing logo (provided).

www.pawsharbourcare.example.au
www.facebook.com/pawsharbourcareau

We wish to clearly communicate our three areas of service "dog minding, home visits, dog walking".

We would like to have the files ready for upload to Printlyne (or similar) for immediate printing.

Target Market(s)

Dog owners who love their dogs like family

Industry/Entity Type

Business

Contact Information for Business Card

Paws Harbour
Ph: 0417 358 904

Font styles to use
Sans Serif

Colors
33a6d7
3176b5

Requirements
Must have
• Logo
• Telephone number
• website
• "Dog minding, home visits, dog walking"
Should not have
• any additional illustrations beyond the logo.

```html
<!DOCTYPE html>
<html lang="en">
<head>
<meta charset="utf-8">
<title>Paws Harbour – Business Card</title>
<link rel="stylesheet" href="https://fonts.googleapis.com/css2?family=Arimo:wght@400;700&display=swap">
<style>
  :root {
    --page: #ffffff;
    --slate: #3a4252;
    --edge-top: #4a5160;
    --edge-bottom: #23272f;
    --service-blue: #2a8fd6;
    --accent-blue: #33a6d7;
    --deep-blue: #3176b5;
    --back-left: #2197d6;
    --back-right: #145d86;
    --white: #ffffff;
  }
  * { box-sizing: border-box; margin: 0; padding: 0; }
  html, body {
    width: 980px; height: 1200px; overflow: hidden;
    background: var(--page);
    font-family: "Arimo", Arial, sans-serif;
  }
  .canvas { position: relative; width: 980px; height: 1200px; }

  .card { position: absolute; left: 2px; width: 976px; overflow: hidden; }
  .card-front { top: 4px; height: 560px; border: 4px solid var(--slate); background: var(--white); }
  .card-back { top: 624px; height: 572px; border: 3px solid #111; background: linear-gradient(90deg, var(--back-left) 0%, #1a7fb6 55%, var(--back-right) 100%); }

  .card-edge {
    position: absolute; left: 0; right: 0; bottom: 0; height: 40px;
    background: linear-gradient(180deg, var(--edge-top), var(--edge-bottom));
  }

  .brand { position: absolute; display: flex; align-items: center; font-weight: 700; white-space: nowrap; }
  .brand-mark { border-radius: 50%; flex: none; }
  .brand-front { left: 0; right: 0; top: 195px; justify-content: center; gap: 22px; color: var(--slate); font-size: 62px; letter-spacing: -0.5px; }
  .brand-front .brand-mark { width: 78px; height: 78px; background: var(--accent-blue); }
  .brand-back { left: 516px; top: 100px; gap: 12px; color: var(--white); font-size: 30px; }
  .brand-back .brand-mark { width: 40px; height: 40px; background: rgba(255,255,255,0.85); }
  .brand-rule { position: absolute; left: 814px; right: 0; top: 132px; height: 2px; background: var(--white); }

  .services {
    position: absolute; left: 0; right: 0; top: 428px;
    display: flex; justify-content: center; gap: 44px;
    list-style: none; color: var(--service-blue);
    font-size: 39px; font-weight: 700;
  }

  .contacts { position: absolute; left: 60px; top: 326px; list-style: none; color: var(--white); }
  .contacts li { display: flex; align-items: baseline; height: 61px; }
  .contact-label { font-size: 17px; margin-right: 10px; }
  .contact-value { font-size: 23px; font-weight: 700; }
  .contacts li:nth-child(2) .contact-label { margin-right: 22px; }
</style>
</head>
<body>
<main class="canvas">
  <section class="card card-front" aria-label="Card front">
    <div class="brand brand-front"><span class="brand-mark"></span>Paws Harbour</div>
    <ul class="services">
      <li>Dog Minding</li>
      <li>Home Visit</li>
      <li>Dog Walking</li>
    </ul>
    <div class="card-edge"></div>
  </section>

  <section class="card card-back" aria-label="Card back">
    <div class="brand brand-back"><span class="brand-mark"></span>Paws Harbour</div>
    <div class="brand-rule"></div>
    <ul class="contacts">
      <li><span class="contact-label">Direct Line</span><span class="contact-value">0417 358 904</span></li>
      <li><span class="contact-label">Website</span><span class="contact-value">pawsharbourcare.example.au</span></li>
      <li><span class="contact-label">Chatterbook</span><span class="contact-value">chatterbook.example / pawsharbourcareau</span></li>
    </ul>
    <div class="card-edge"></div>
  </section>
</main>
</body>
</html>
```